bramblegate crest roofing flyer*

I need an a5 size flyer designing to go in our local advertising magazine.We are based in the north west of England Id like key features from the website including on the flyer, possibly even reviews, what we do ect.I don't however want it too busy, simple pictures and description of service.company colours and logo. I require simple one sided business cards toonumber, web address and logowinner will receive a request to design around 5 different double sided a5 flyers too, each with all our services on one side and the other primarily for one service we have provided locally with a spacve to put the house number down.REPAIRSROOFLINEFLAT ROOFS PITCHED ROOFSSYNTHETIC ROOFSUP TO 50 YEARS WARRANTY AVAILABLERANKED THE #1 FLAT ROOFER IN THE UK OUT OF 787 REGISTERED FLAT ROOFING COMPANIESRANKED THE #10 ROOFING COMPANY IN THE UK OUT OF 1976 REGISTERED SPECIALIST ROOFING COMPANIESBOTH FOR COST, CUSTOMER SERVICE AND QUALITY WITH 5 STAR REVIEWSGUARANTEED TO FIND AND FIX A LEAKAPPROVED INSTALLERSAWARD WINNINGTIME SERVED FIXED PRICES

Target Market(s)

homeowners

Colors

Designer to choose only greyscale colors for use in the design.

Requirements
Must have
• contact details
• pictures of my work
• clear and simple

```html
<!DOCTYPE html>
<html lang="en">
<head>
<meta charset="utf-8">
<title>Bramblegate Crest Roofing – Eco Roofing Slate Flyer</title>
<link href="https://fonts.googleapis.com/css2?family=Oswald:wght@500;700&family=Open+Sans:wght@400;600;700&display=swap" rel="stylesheet">
<style>
  :root {
    --page-bg: #e4e4e4;
    --paper: #ffffff;
    --green-dark: #2f6d1d;
    --green: #4a9a2a;
    --green-light: #8cc63f;
    --yellow: #f4c51c;
    --ink: #1d1d1d;
    --ink-soft: #4a4a4a;
    --gold: #c9a23a;
    --gold-dark: #8a6a16;
  }
  * { box-sizing: border-box; margin: 0; padding: 0; }
  html, body { width: 784px; height: 1200px; overflow: hidden; }
  body { background: var(--page-bg); font-family: "Open Sans", Arial, sans-serif; color: var(--ink); }

  .flyer {
    position: absolute; left: 12px; top: 62px;
    width: 760px; height: 1075px;
    background: var(--paper);
    overflow: hidden;
    box-shadow: 0 2px 10px rgba(0,0,0,.15);
  }

  /* Header */
  .header { position: absolute; left: 0; top: 0; width: 100%; height: 170px; }
  .brand {
    position: absolute; left: 36px; top: 40px;
    display: flex; align-items: center; gap: 10px;
  }
  .brand-dot { width: 18px; height: 18px; border-radius: 50%; background: var(--green); }
  .brand-name {
    font-family: "Oswald", Arial, sans-serif; font-weight: 700;
    font-size: 26px; line-height: 1.05; color: var(--green-dark);
    text-transform: uppercase; width: 190px;
  }
  .headline { position: absolute; left: 290px; top: 26px; }
  .headline-title {
    font-family: "Oswald", Arial, sans-serif; font-weight: 700;
    font-size: 54px; line-height: .98; color: var(--ink); text-transform: uppercase;
  }
  .headline-title .accent { color: var(--green); }
  .headline-sub { margin-top: 10px; font-size: 17px; font-weight: 600; color: var(--ink-soft); }

  /* Photo */
  .hero-photo {
    position: absolute; left: 0; top: 170px; width: 100%; height: 400px;
    background: linear-gradient(180deg, #dfe9f1 0%, #b9cbd8 30%, #8f9a8a 55%, #6b7d55 72%, #4f8a2c 100%);
  }

  /* Green section */
  .lower {
    position: absolute; left: 0; top: 560px; width: 100%; height: 515px;
    background: linear-gradient(180deg, var(--green-light) 0%, var(--green) 45%, var(--green-dark) 100%);
  }
  .features-band {
    position: absolute; left: 50%; top: 20px; transform: translateX(-50%);
    background: var(--yellow); padding: 8px 48px;
    font-family: "Oswald", Arial, sans-serif; font-weight: 700; font-size: 24px;
    color: var(--green-dark); letter-spacing: 1px; text-transform: uppercase;
  }
  .feature-list {
    position: absolute; left: 40px; top: 78px; width: 680px;
    display: grid; grid-template-columns: 1fr 1fr; column-gap: 30px; row-gap: 9px;
    list-style: none;
  }
  .feature-list li {
    display: flex; align-items: center; gap: 8px;
    font-size: 13px; color: #fff; font-weight: 600;
  }
  .feature-list svg { flex: 0 0 16px; }

  .claims {
    position: absolute; left: 40px; top: 262px; width: 680px;
    display: grid; grid-template-columns: repeat(4, 1fr); gap: 16px;
  }
  .claim {
    background: var(--paper); border-radius: 8px;
    height: 96px; padding: 12px 10px 30px;
    text-align: center; font-size: 12px; font-weight: 700; line-height: 1.3; color: var(--ink);
  }
  .seals {
    position: absolute; left: 40px; top: 330px; width: 680px;
    display: grid; grid-template-columns: repeat(4, 1fr); gap: 16px; justify-items: center;
  }
  .seal {
    width: 86px; height: 86px; border-radius: 50%;
    background: radial-gradient(circle at 40% 35%, #f3dc86 0%, var(--gold) 55%, var(--gold-dark) 100%);
    border: 4px solid #e9d08a;
  }

  .contact {
    position: absolute; left: 0; bottom: 0; width: 100%; height: 74px;
    background: rgba(0,0,0,.18);
    display: flex; align-items: center; justify-content: space-between; padding: 0 36px;
    color: #fff;
  }
  .contact-phone {
    display: flex; align-items: center; gap: 8px;
    font-family: "Oswald", Arial, sans-serif; font-weight: 700; font-size: 24px; color: var(--yellow);
  }
  .contact-details { font-size: 13px; line-height: 1.5; text-align: right; font-weight: 600; }
</style>
</head>
<body>
  <article class="flyer">
    <header class="header">
      <div class="brand">
        <span class="brand-dot"></span>
        <span class="brand-name">Bramblegate Crest Roofing</span>
      </div>
      <div class="headline">
        <h1 class="headline-title">The Eco<br><span class="accent">Roffing Slate</span></h1>
        <p class="headline-sub">Ideal For Pitches As Low As 10 Degree</p>
      </div>
    </header>

    <div class="hero-photo" role="img" aria-label="Photograph of a large detached house with a newly fitted grey slate roof, surrounded by trees and a green lawn"></div>

    <section class="lower">
      <h2 class="features-band">Features &amp; Benefits</h2>

      <ul class="feature-list">
        <li><svg width="16" height="16" viewBox="0 0 16 16"><rect width="16" height="16" rx="3" fill="#f4c51c"/><path d="M4 8.5l2.5 2.5L12 5.5" stroke="#2f6d1d" stroke-width="2" fill="none"/></svg>Guaranteed to find and fix a leak</li>
        <li><svg width="16" height="16" viewBox="0 0 16 16"><rect width="16" height="16" rx="3" fill="#f4c51c"/><path d="M4 8.5l2.5 2.5L12 5.5" stroke="#2f6d1d" stroke-width="2" fill="none"/></svg>Ranked #1 flat roofer in the UK</li>
        <li><svg width="16" height="16" viewBox="0 0 16 16"><rect width="16" height="16" rx="3" fill="#f4c51c"/><path d="M4 8.5l2.5 2.5L12 5.5" stroke="#2f6d1d" stroke-width="2" fill="none"/></svg>Up to 50 years warranty available</li>
        <li><svg width="16" height="16" viewBox="0 0 16 16"><rect width="16" height="16" rx="3" fill="#f4c51c"/><path d="M4 8.5l2.5 2.5L12 5.5" stroke="#2f6d1d" stroke-width="2" fill="none"/></svg>Ranked #10 roofing company in UK</li>
        <li><svg width="16" height="16" viewBox="0 0 16 16"><rect width="16" height="16" rx="3" fill="#f4c51c"/><path d="M4 8.5l2.5 2.5L12 5.5" stroke="#2f6d1d" stroke-width="2" fill="none"/></svg>Approved installers you can trust</li>
        <li><svg width="16" height="16" viewBox="0 0 16 16"><rect width="16" height="16" rx="3" fill="#f4c51c"/><path d="M4 8.5l2.5 2.5L12 5.5" stroke="#2f6d1d" stroke-width="2" fill="none"/></svg>5 star reviews for quality and service</li>
        <li><svg width="16" height="16" viewBox="0 0 16 16"><rect width="16" height="16" rx="3" fill="#f4c51c"/><path d="M4 8.5l2.5 2.5L12 5.5" stroke="#2f6d1d" stroke-width="2" fill="none"/></svg>Award winning local roofing team</li>
        <li><svg width="16" height="16" viewBox="0 0 16 16"><rect width="16" height="16" rx="3" fill="#f4c51c"/><path d="M4 8.5l2.5 2.5L12 5.5" stroke="#2f6d1d" stroke-width="2" fill="none"/></svg>Repairs, roofline and flat roofs</li>
        <li><svg width="16" height="16" viewBox="0 0 16 16"><rect width="16" height="16" rx="3" fill="#f4c51c"/><path d="M4 8.5l2.5 2.5L12 5.5" stroke="#2f6d1d" stroke-width="2" fill="none"/></svg>Time served roofers, fixed prices</li>
        <li><svg width="16" height="16" viewBox="0 0 16 16"><rect width="16" height="16" rx="3" fill="#f4c51c"/><path d="M4 8.5l2.5 2.5L12 5.5" stroke="#2f6d1d" stroke-width="2" fill="none"/></svg>Pitched and synthetic roofs fitted</li>
      </ul>

      <div class="claims">
        <p class="claim">Ranked #1 Flat Roofer Out Of 787</p>
        <p class="claim">Ranked #10 Roofer Out Of 1976</p>
        <p class="claim">Both For Cost, Service &amp; Quality</p>
        <p class="claim">Up To 50 Years Warranty Available</p>
      </div>
      <div class="seals">
        <span class="seal"></span>
        <span class="seal"></span>
        <span class="seal"></span>
        <span class="seal"></span>
      </div>

      <footer class="contact">
        <div class="contact-phone">
          <svg width="22" height="22" viewBox="0 0 24 24"><path fill="#f4c51c" d="M6.6 10.8a15.1 15.1 0 006.6 6.6l2.2-2.2a1 1 0 011-.25 11.4 11.4 0 003.6.57 1 1 0 011 1V20a1 1 0 01-1 1A17 17 0 013 4a1 1 0 011-1h3.5a1 1 0 011 1c0 1.25.2 2.45.57 3.6a1 1 0 01-.25 1z"/></svg>
          Call 0161 496 0732
        </div>
        <div class="contact-details">
          12 Moss Lane, Warrington<br>
          hello@bramblegatecrest.co.uk<br>
          www.bramblegatecrest.co.uk
        </div>
      </footer>
    </section>
  </article>
</body>
</html>
```